Brindle Pet Shop Homepage

We are a pet shop, we focus on dog food / cat food / rodents & bird food

Based on WooCommerce

It should be a simple but professional homepage with an informative start page. In the shop it should then be possible to shop for products/manufacturers etc. Navigation/Filter menu on the left would be ideal.

Next menus:
ABOUT US
CONTACT
DOG
CAT
HOLDER

My Account - Login
My Cart

Footer:
Conditions
payment options
social media

In addition to our logo, I have attached 2 example pages from another shop which we would use as a guideline.

Target Market(s)

pet store

Industry/Entity Type

Animal, Pet Shop

Coding

Coded - Design and coding required

Number of Pages Required

1 page

Font styles to use
Sans Serif

Colors
0054AA
0677BA
7BADD7
CADEEF
E8F1F8

Requirements
Must have
• Main Page, Contact, About Us, Shop, Check Out, Member Login, Mailchimp Marketing - We work with WooCommerce

```html
<!DOCTYPE html>
<html lang="en">
<head>
<meta charset="utf-8">
<title>Brindle Pet Shop – Premium Pet Food</title>
<link rel="stylesheet" href="https://fonts.googleapis.com/css2?family=Baloo+2:wght@600;700;800&family=Caveat:wght@500;700&family=Nunito+Sans:wght@400;600;700;800&display=swap">
<style>
:root{
  --blue:#1672d6;
  --blue-deep:#0054AA;
  --blue-mid:#0677BA;
  --blue-soft:#7BADD7;
  --blue-pale:#CADEEF;
  --blue-mist:#E8F1F8;
  --hero-bg:#f3f7fc;
  --navy:#2f3a5c;
  --ink:#2b2b38;
  --muted:#6b7080;
  --orange:#e8704a;
  --band:#f1f1f2;
  --line:#d9dbe0;
  --star:#f5b300;
  --footer:#22223a;
  --white:#ffffff;
}
*{box-sizing:border-box;margin:0;padding:0}
html,body{width:1200px;height:4747px;overflow:hidden}
body{position:relative;background:var(--white);font-family:"Nunito Sans",Arial,sans-serif;color:var(--ink)}
.abs{position:absolute}
.display{font-family:"Baloo 2","Trebuchet MS",sans-serif;font-weight:800;color:var(--navy);letter-spacing:.3px}
.script{font-family:"Caveat",cursive;color:var(--orange);font-weight:500}
.btn{position:absolute;display:flex;align-items:center;justify-content:center;background:var(--blue);color:var(--white);border-radius:4px;font-weight:800;font-size:16px;box-shadow:0 6px 14px rgba(22,114,214,.25)}
.ph{position:absolute;border-radius:10px}

/* header */
.hero{left:0;top:0;width:1200px;height:700px;background:var(--hero-bg)}
.logo{display:flex;align-items:center;gap:10px}
.logo-mark{width:42px;height:42px;border-radius:50%;background:var(--blue)}
.logo-text{font-weight:800;font-size:22px;color:var(--blue);letter-spacing:1px}
.logo-sub{position:absolute;left:63px;top:38px;font-size:11px;letter-spacing:2px;color:var(--navy);white-space:nowrap}
.nav{left:512px;top:42px;display:flex;gap:34px;font-size:14px;font-weight:600;color:var(--navy)}
.nav span{display:flex;align-items:center;gap:8px}
.hero-title{left:85px;top:186px;font-size:54px;line-height:61px}
.hero-title .accent{color:var(--blue)}
.hero-copy{left:85px;top:394px;width:300px;font-size:14px;line-height:24px;color:var(--ink)}
.shop-now{left:85px;top:462px;width:210px;height:60px;justify-content:space-between;padding:0 18px;font-size:16px}
.shop-now small{display:block;font-size:11px;font-weight:400;opacity:.8}
.secure{left:85px;top:532px;font-size:12px;display:flex;align-items:center;gap:8px}
.avatars{left:85px;top:582px;display:flex}
.avatars i{width:40px;height:40px;border-radius:50%;background:#c9a48a;border:3px solid var(--white);margin-right:-10px}
.rating{left:198px;top:586px;display:flex;align-items:center;gap:12px}
.rating b{font-size:20px;color:var(--navy)}
.stars{color:var(--star);font-size:16px;letter-spacing:1px}

/* stats band */
.band{left:0;top:787px;width:1200px;height:85px;background:var(--band);display:flex;justify-content:center;gap:0}
.stat{position:absolute;top:14px;display:flex;align-items:center;gap:16px}
.stat .big{font-family:"Baloo 2",sans-serif;font-weight:800;font-size:50px;color:var(--navy);line-height:1}
.stat .lbl{font-size:13px;color:var(--navy);font-weight:600;line-height:18px}
.stat .lbl span{display:block;color:var(--muted);font-weight:400;font-size:12px}

.section-title{width:1200px;left:0;text-align:center;font-size:52px;line-height:60px}
.paw{width:70px;height:62px}

/* tabs */
.tabs{left:105px;top:1156px;display:flex;gap:12px}
.tab{width:190px;height:57px;border:1px solid var(--line);border-radius:4px;display:flex;align-items:center;justify-content:center;gap:10px;font-size:15px;font-weight:700;color:var(--navy);background:var(--white);box-shadow:0 4px 10px rgba(0,0,0,.05)}
.tab i{width:24px;height:24px;border-radius:6px;background:var(--blue-mist)}
.tab.active{background:var(--blue);color:var(--white);border-color:var(--blue)}
.tab.active i{background:#ffd36b}

.card{position:absolute;border:2px solid var(--line);border-radius:6px;background:var(--white)}
.heart{position:absolute;right:12px;top:12px;width:34px;height:34px;border-radius:50%;border:1px solid var(--line);display:flex;align-items:center;justify-content:center}
.heart.on{background:var(--blue);border-color:var(--blue)}
.plus{position:absolute;right:30px;bottom:30px;width:40px;height:40px;border-radius:50%;border:2px solid var(--line);display:flex;align-items:center;justify-content:center;font-size:20px;color:var(--navy)}
.p-name{position:absolute;left:14px;bottom:50px;font-size:14px;font-weight:600;color:var(--navy)}
.p-price{position:absolute;left:14px;bottom:22px;font-size:15px;font-weight:800;color:var(--blue)}
.arrow{position:absolute;width:54px;height:54px;border-radius:50%;display:flex;align-items:center;justify-content:center}
.arrow.light{background:var(--white);border:1px solid var(--line);box-shadow:0 4px 10px rgba(0,0,0,.08)}
.arrow.dark{background:var(--blue)}

/* premium */
.premium{left:0;top:1793px;width:1200px;height:489px;background:var(--hero-bg)}
.cat-list{left:85px;top:2022px;font-size:14px;line-height:40px;color:var(--ink)}

.best .btn{width:197px;height:57px;font-size:16px;gap:10px}

.different{left:0;top:3017px;width:1200px;height:660px;background:var(--hero-bg)}

.badge-new{position:absolute;left:-2px;top:-2px;width:46px;height:46px;background:var(--orange);border-radius:0 0 46px 0;color:var(--white);font-size:11px;font-weight:800;padding:10px 0 0 6px}

/* footer */
.footer{left:0;top:4307px;width:1200px;height:440px;background:var(--footer);color:var(--white)}
.f-col{position:absolute;top:108px;font-size:14px}
.f-col h4{font-size:15px;font-weight:800;font-style:italic;margin-bottom:26px}
.f-col p{margin-bottom:23px;color:#d8d9e4}
.social{display:flex;gap:12px}
.social i{width:34px;height:34px;border-radius:50%;background:var(--blue)}
.pay{display:flex;align-items:center;gap:8px;font-weight:800;font-style:italic;font-size:15px}
.pay i{width:28px;height:14px;border-radius:2px;background:#dfe3ea}
</style>
</head>
<body>

<!-- HERO -->
<section class="abs hero">
  <div class="abs logo" style="left:85px;top:32px">
    <span class="logo-mark"></span><span class="logo-text">BRINDLE PET</span>
    <span class="logo-sub">PREMIUM PET FOOD</span>
  </div>
  <nav class="abs nav">
    <span>ABOUT US</span><span>CONTACT</span><span>DOG</span><span>CAT</span><span>HOLDER</span>
    <span><svg width="14" height="14" viewBox="0 0 14 14"><path d="M2 5h10l-1 8H3z" fill="#1672d6"/><path d="M4.5 5V3.5a2.5 2.5 0 015 0V5" stroke="#1672d6" stroke-width="1.5" fill="none"/></svg>Cart</span>
    <span><svg width="14" height="14" viewBox="0 0 14 14"><circle cx="7" cy="4" r="3" fill="#1672d6"/><path d="M1 14a6 5 0 0112 0z" fill="#1672d6"/></svg>Login</span>
  </nav>
  <div class="abs script" style="left:85px;top:146px;font-size:32px">100% Natural</div>
  <h1 class="abs display hero-title">Healthy &amp;<br><span class="accent">Natural Pet</span><br>Food</h1>
  <div class="ph" role="img" aria-label="Small cartoon puppy illustration" style="left:322px;top:192px;width:44px;height:44px;border-radius:50%;background:var(--blue-pale)"></div>
  <div class="ph" role="img" aria-label="Dog face emoji" style="left:208px;top:318px;width:42px;height:42px;border-radius:50%;background:#e6a84a"></div>
  <p class="abs hero-copy">Lorem ipsum dolor sit amet, consectetur adipiscing elitnas eu consequat</p>
  <div class="btn shop-now"><span>Shop Now<small>Upto 20% off</small></span><span>$ 38.00</span></div>
  <div class="abs secure"><svg width="12" height="13" viewBox="0 0 12 13"><rect x="1" y="6" width="10" height="7" rx="1" fill="#2b2b38"/><path d="M3 6V4a3 3 0 016 0v2" stroke="#2b2b38" stroke-width="1.6" fill="none"/></svg>100% secure payment</div>
  <div class="abs avatars" role="img" aria-label="Customer portraits"><i></i><i style="background:#b88a6c"></i><i style="background:#d4b09a"></i></div>
  <div class="abs rating"><b>5.0</b><span style="width:1px;height:26px;background:var(--line)"></span><span><span class="stars">★★★★★</span><br><span style="font-size:11px;color:var(--muted)">+255 Reviews</span></span></div>
  <div class="ph" role="img" aria-label="Beagle sitting beside a red pet food bag and a steel bowl of kibble, with kibble pieces flying" style="left:470px;top:100px;width:730px;height:560px;border-radius:0;background:radial-gradient(ellipse at 65% 55%,#d99a62 0%,#c8644c 28%,#eef2f7 62%,var(--hero-bg) 80%)"></div>
  <div class="ph" role="img" aria-label="Doctor approved badge" style="left:574px;top:406px;width:90px;height:90px;border-radius:50%;background:var(--white);border:3px solid var(--blue)"></div>
</section>

<!-- STATS -->
<section class="abs band">
  <div class="stat" style="left:212px"><span class="big">#1</span><span class="lbl">PREMIUM<span>Pet Food</span></span></div>
  <div class="stat" style="left:479px"><span class="big">0%</span><span class="lbl">FILLERS<span>Pet Food</span></span></div>
  <div class="stat" style="left:752px"><span class="big">NO</span><span class="lbl">ARTIFICAL FLAVORS<span>Or preservatives</span></span></div>
</section>

<!-- LATEST TABS -->
<h2 class="abs display section-title" style="top:988px">Get the valuable pet Food<br>of lastest products</h2>
<svg class="abs paw" style="left:990px;top:1025px" viewBox="0 0 70 62"><g fill="#dfe7f2"><ellipse cx="35" cy="44" rx="16" ry="14"/><ellipse cx="12" cy="26" rx="7" ry="9"/><ellipse cx="26" cy="10" rx="7" ry="9"/><ellipse cx="44" cy="10" rx="7" ry="9"/><ellipse cx="58" cy="26" rx="7" ry="9"/></g></svg>
<div class="abs tabs">
  <div class="tab active"><i></i>All Products</div>
  <div class="tab"><i></i>Dog Food</div>
  <div class="tab"><i></i>Cat Food</div>
  <div class="tab"><i></i>Rodents Food</div>
  <div class="tab"><i></i>Bird Food</div>
</div>

<div class="card" style="left:85px;top:1277px;width:245px;height:387px">
  <div class="heart"><svg width="14" height="12" viewBox="0 0 14 12"><path d="M7 11L1.5 5.5a3 3 0 015-4L7 2l.5-.5a3 3 0 015 4z" fill="none" stroke="#9aa0ad" stroke-width="1.3"/></svg></div>
  <div class="ph" role="img" aria-label="Blue bag of premium cat food with a cat photo" style="left:45px;top:58px;width:150px;height:180px;background:linear-gradient(#2f6fc0,#c58b55)"></div>
  <div class="p-name">Premum Cat Food</div><div class="p-price">$ 36.00</div><div class="plus">+</div>
</div>
<div class="card" style="left:346px;top:1277px;width:245px;height:387px">
  <div class="heart on"><svg width="14" height="12" viewBox="0 0 14 12"><path d="M7 11L1.5 5.5a3 3 0 015-4L7 2l.5-.5a3 3 0 015 4z" fill="#fff"/></svg></div>
  <div class="ph" role="img" aria-label="Yellow bag of premium dog food with a dog photo" style="left:45px;top:58px;width:150px;height:180px;background:linear-gradient(#d8aa3e,#b98a45)"></div>
  <div class="p-name">Premium Dog Food</div><div class="p-price">$ 36.00</div><div class="plus">+</div>
</div>
<div class="card" style="left:607px;top:1277px;width:245px;height:387px">
  <div class="heart"><svg width="14" height="12" viewBox="0 0 14 12"><path d="M7 11L1.5 5.5a3 3 0 015-4L7 2l.5-.5a3 3 0 015 4z" fill="none" stroke="#9aa0ad" stroke-width="1.3"/></svg></div>
  <div class="ph" role="img" aria-label="Dark green bag of premium bird food with a parrot photo" style="left:45px;top:58px;width:150px;height:180px;background:linear-gradient(#2f4a33,#3c8a3a)"></div>
  <div class="p-name">Premum Bird Food</div><div class="p-price">$ 36.00</div><div class="plus">+</div>
</div>
<div class="card" style="left:868px;top:1277px;width:245px;height:387px">
  <div class="heart"><svg width="14" height="12" viewBox="0 0 14 12"><path d="M7 11L1.5 5.5a3 3 0 015-4L7 2l.5-.5a3 3 0 015 4z" fill="none" stroke="#9aa0ad" stroke-width="1.3"/></svg></div>
  <div class="ph" role="img" aria-label="Orange bag of premium rodents food with a rabbit photo" style="left:45px;top:58px;width:150px;height:180px;background:linear-gradient(#e0832f,#8a6a55)"></div>
  <div class="p-name">Premum Rodents Food</div><div class="p-price">$ 36.00</div><div class="plus">+</div>
</div>
<div class="arrow light" style="left:58px;top:1436px"><svg width="12" height="14"><path d="M9 2L3 7l6 5" stroke="#1672d6" stroke-width="2.4" fill="none"/></svg></div>
<div class="arrow dark" style="left:1081px;top:1436px"><svg width="12" height="14"><path d="M3 2l6 5-6 5" stroke="#fff" stroke-width="2.4" fill="none"/></svg></div>

<!-- PREMIUM -->
<section class="abs premium">
  <div class="abs script" style="left:85px;top:106px;font-size:34px">Premium</div>
  <div class="abs display" style="left:85px;top:152px;font-size:50px">Pet Food</div>
  <div class="ph" role="img" aria-label="Three pet food bags: dog, cat and a green dog food bag" style="left:341px;top:124px;width:479px;height:317px;background:linear-gradient(90deg,#e9c48a 0%,#6fa5b8 50%,#2f7a82 100%)"></div>
  <div class="abs" style="left:925px;top:186px;font-size:18px;color:var(--blue);font-weight:700">From $ 20.00</div>
  <div class="abs" style="left:970px;top:220px;font-size:18px;color:var(--orange);font-weight:700;text-decoration:line-through">To $ 85.00</div>
  <div class="btn" style="left:900px;top:273px;width:193px;height:59px">Shop Now</div>
  <svg class="abs paw" style="left:912px;top:372px" viewBox="0 0 70 62"><g fill="#dfe7f2"><ellipse cx="35" cy="44" rx="16" ry="14"/><ellipse cx="12" cy="26" rx="7" ry="9"/><ellipse cx="26" cy="10" rx="7" ry="9"/><ellipse cx="44" cy="10" rx="7" ry="9"/><ellipse cx="58" cy="26" rx="7" ry="9"/></g></svg>
</section>
<div class="abs cat-list"><div>› Dog food</div><div>› Cat food</div><div>› Rodents</div><div>› Bird food</div></div>

<!-- BEST SELLING -->
<h2 class="abs display section-title" style="top:2403px">Best Selling Products</h2>
<div class="best">
  <div class="card" style="left:85px;top:2507px;width:333px;height:381px">
    <div class="heart"><svg width="14" height="12" viewBox="0 0 14 12"><path d="M7 11L1.5 5.5a3 3 0 015-4L7 2l.5-.5a3 3 0 015 4z" fill="none" stroke="#9aa0ad" stroke-width="1.3"/></svg></div>
    <div class="ph" role="img" aria-label="Cat food pouch with kibble window" style="left:100px;top:28px;width:130px;height:210px;background:linear-gradient(#f0e4d8,#3f66b8 60%,#e0712f)"></div>
    <div class="abs" style="left:42px;top:264px;font-weight:800;font-size:16px;color:var(--navy)">Cat Food</div>
    <div class="abs" style="left:202px;top:262px;font-weight:700;font-size:16px;color:var(--blue)">$ 36.00</div>
    <div class="btn" style="left:54px;top:302px">🔒︎ Add To Cart</div>
  </div>
  <div class="card" style="left:434px;top:2507px;width:333px;height:381px">
    <div class="heart"><svg width="14" height="12" viewBox="0 0 14 12"><path d="M7 11L1.5 5.5a3 3 0 015-4L7 2l.5-.5a3 3 0 015 4z" fill="none" stroke="#9aa0ad" stroke-width="1.3"/></svg></div>
    <div class="ph" role="img" aria-label="Cat food pouch with kibble window" style="left:100px;top:28px;width:130px;height:210px;background:linear-gradient(#f0e4d8,#3f66b8 60%,#e0712f)"></div>
    <div class="abs" style="left:42px;top:264px;font-weight:800;font-size:16px;color:var(--navy)">Cat Food</div>
    <div class="abs" style="left:202px;top:262px;font-weight:700;font-size:16px;color:var(--blue)">$ 36.00</div>
    <div class="btn" style="left:54px;top:302px">🔒︎ Add To Cart</div>
  </div>
  <div class="card" style="left:783px;top:2507px;width:333px;height:381px">
    <div class="heart"><svg width="14" height="12" viewBox="0 0 14 12"><path d="M7 11L1.5 5.5a3 3 0 015-4L7 2l.5-.5a3 3 0 015 4z" fill="none" stroke="#9aa0ad" stroke-width="1.3"/></svg></div>
    <div class="ph" role="img" aria-label="Cat food pouch with kibble window" style="left:100px;top:28px;width:130px;height:210px;background:linear-gradient(#f0e4d8,#3f66b8 60%,#e0712f)"></div>
    <div class="abs" style="left:42px;top:264px;font-weight:800;font-size:16px;color:var(--navy)">Cat Food</div>
    <div class="abs" style="left:202px;top:262px;font-weight:700;font-size:16px;color:var(--blue)">$ 36.00</div>
    <div class="btn" style="left:54px;top:302px">🔒︎ Add To Cart</div>
  </div>
</div>

<!-- DIFFERENT -->
<section class="abs different">
  <div class="abs script" style="left:85px;top:122px;font-size:32px">What makes us</div>
  <h2 class="abs display" style="left:85px;top:168px;font-size:52px;line-height:60px">Different from<br>others</h2>
  <p class="abs" style="left:87px;top:308px;width:360px;font-size:14px;line-height:24px">Donec tristique mi pellentesque tempor volutpat. Donec lobortis tortortricies dolor dictum aliquet. Class aptent taciti sociosqu ad litora torquent per conubia nostra, per inceptos himenaeos. Cras sodales purus nec dolor iaculis accumsan. Morbi egestas tempor dui eu tempus.</p>
  <div class="btn" style="left:87px;top:481px;width:184px;height:58px">Learn More</div>
  <div class="ph" role="img" aria-label="Speech bubble reading 100% organic pet food" style="left:716px;top:84px;width:200px;height:170px;border-radius:50%;background:var(--white);border:2px solid var(--navy)"></div>
  <div class="ph" role="img" aria-label="Three pet food bags beside a kitten and a beagle" style="left:452px;top:240px;width:681px;height:340px;background:linear-gradient(90deg,#e7ebf2 0%,#3f9a55 35%,#e7ebf2 55%,#d9985a 78%,#b87a4a 100%)"></div>
</section>

<!-- LATEST PRODUCT -->
<h2 class="abs display section-title" style="top:3796px">Latest Product</h2>
<p class="abs" style="left:0;width:1200px;top:3870px;text-align:center;font-size:14px">Lorem ipsum dolor sit amet, consectetur adipiscing elitnas eu consequat</p>
<svg class="abs paw" style="left:900px;top:3830px" viewBox="0 0 70 62"><g fill="#dfe7f2"><ellipse cx="35" cy="44" rx="16" ry="14"/><ellipse cx="12" cy="26" rx="7" ry="9"/><ellipse cx="26" cy="10" rx="7" ry="9"/><ellipse cx="44" cy="10" rx="7" ry="9"/><ellipse cx="58" cy="26" rx="7" ry="9"/></g></svg>
<div class="card" style="left:87px;top:3935px;width:330px;height:278px">
  <span class="badge-new">NEW</span>
  <div class="ph" role="img" aria-label="Teal cat food bag mockup" style="left:125px;top:22px;width:80px;height:130px;background:linear-gradient(#5fa9bf,#3a4b5a)"></div>
  <div class="abs" style="left:16px;top:208px;font-size:18px;color:var(--navy)">Premum Cat Food</div>
  <div class="abs stars" style="right:12px;top:202px">★★★★★</div>
  <div class="abs" style="right:22px;top:228px;font-size:12px;color:var(--muted)">(12 Reviews)</div>
</div>
<div class="card" style="left:435px;top:3935px;width:330px;height:278px">
  <div class="ph" role="img" aria-label="Red dog food bag mockup" style="left:125px;top:22px;width:80px;height:130px;background:linear-gradient(#d64040,#9a3030)"></div>
  <div class="abs" style="left:16px;top:208px;font-size:18px;color:var(--navy)">Dog Food</div>
  <div class="abs stars" style="right:12px;top:202px">★★★★★</div>
  <div class="abs" style="right:22px;top:228px;font-size:12px;color:var(--muted)">(12 Reviews)</div>
</div>
<div class="card" style="left:783px;top:3935px;width:330px;height:278px">
  <span class="badge-new">NEW</span>
  <div class="ph" role="img" aria-label="Teal cat food bag mockup" style="left:125px;top:22px;width:80px;height:130px;background:linear-gradient(#5fa9bf,#3a4b5a)"></div>
  <div class="abs" style="left:16px;top:208px;font-size:18px;color:var(--navy)">Premum Cat Food</div>
  <div class="abs stars" style="right:12px;top:202px">★★★★★</div>
  <div class="abs" style="right:22px;top:228px;font-size:12px;color:var(--muted)">(12 Reviews)</div>
</div>
<div class="arrow light" style="left:60px;top:4045px"><svg width="12" height="14"><path d="M9 2L3 7l6 5" stroke="#1672d6" stroke-width="2.4" fill="none"/></svg></div>
<div class="arrow dark" style="left:1081px;top:4045px"><svg width="12" height="14"><path d="M3 2l6 5-6 5" stroke="#fff" stroke-width="2.4" fill="none"/></svg></div>

<!-- FOOTER -->
<footer class="abs footer">
  <div class="abs" style="left:85px;top:132px;display:flex;align-items:center;gap:12px">
    <span style="width:52px;height:52px;border-radius:50%;background:var(--white)"></span>
    <span style="font-size:28px;font-weight:800;letter-spacing:1px">BRINDLE PET</span>
  </div>
  <div class="abs" style="left:150px;top:192px;font-size:15px;letter-spacing:2px">PREMIUM PET FOOD</div>
  <div class="f-col" style="left:439px"><h4>Account Login</h4><p>Create Account</p><p>Orders</p><p>Favorites List</p><p>Comparison</p></div>
  <div class="f-col" style="left:695px"><h4>Information</h4><p>Home</p><p>Teram and Condition</p><p>Privacy Policy</p><p>Company</p></div>
  <div class="f-col" style="left:946px"><h4>Follow Us</h4>
    <div class="social" style="margin-top:-6px"><i></i><i></i><i></i></div>
    <h4 style="margin-top:38px;margin-bottom:14px">Follow Us</h4>
    <div class="pay">PayNest <i></i><i></i><i></i><i></i></div>
  </div>
  <div class="abs" style="left:85px;top:400px;font-size:14px;color:#c8c9d6">© 2023 <span style="color:var(--blue-soft)">Brindle Pet</span>. All right reserved</div>
</footer>

</body>
</html>
```